Powerpoint template for Meadowlark Crossing

I need a powerpoint template for my business that would also work for Google slides.
I intermittently deliver training to people and I want a nice powerpoint template, that could also work in google docs to help make production easier and more seamless for me. I also sometimes product reports and analyses that are best done in powerpoint or Google slides. I need a title page, Title and content page, section heading page and any other pages that someone normally has!

Target Market(s)

Leaders and managers in medium to large companies. I provide training and coaching services to senior staff who have got 'stuck' and want help to find their way forward.

Font styles to use
Sans Serif

Requirements
Must have
• Colours and fonts to fit with logo please.
• Must include the logo and company name.
Nice to have
• a picture for the front?

```html
<!DOCTYPE html>
<html lang="en">
<head>
<meta charset="utf-8">
<title>Meadowlark Crossing – Presentation Template</title>
<link href="https://fonts.googleapis.com/css2?family=Raleway:wght@500;600;700&family=Open+Sans:wght@400;600;700&display=swap" rel="stylesheet">
<style>
  :root{
    --purple:#4a2c90;
    --teal:#1db596;
    --ink:#111111;
    --grey-text:#6f6f6f;
    --canvas-top:#f1f1f1;
    --canvas-bottom:#9e9e9e;
    --white:#ffffff;
  }
  *{box-sizing:border-box;margin:0;padding:0}
  html,body{width:748px;height:1200px;overflow:hidden}
  body{position:relative;background:var(--canvas-bottom);font-family:"Open Sans",sans-serif;color:var(--ink)}
  .stage-top{position:absolute;left:0;top:0;width:748px;height:502px;background:var(--canvas-top)}
  .slide{position:absolute;width:340px;height:191px;background:var(--white);overflow:hidden;box-shadow:0 6px 10px rgba(0,0,0,.28)}
  .slide--hero{left:110px;top:100px;transform:scale(1.55);transform-origin:0 0;box-shadow:0 4px 8px rgba(0,0,0,.12)}
  .pos-1{left:22px;top:538px}.pos-2{left:386px;top:538px}
  .pos-3{left:22px;top:761px}.pos-4{left:386px;top:761px}
  .pos-5{left:22px;top:980px}.pos-6{left:386px;top:980px}

  /* title slide */
  .cover-photo{position:absolute;left:60px;top:0;width:280px;height:191px;
    background:linear-gradient(90deg,#ffffff 0%,rgba(255,255,255,0) 35%),
      linear-gradient(180deg,rgba(255,255,255,0) 60%,#ffffff 100%),
      linear-gradient(120deg,#9fb08c 0%,#6f8a5c 35%,#d9c7c0 60%,#e9e6e2 100%)}
  .cover-brand{position:absolute;left:10px;top:72px;display:flex;align-items:center;gap:4px}
  .brand-dot{width:7px;height:7px;border-radius:50%;background:var(--teal)}
  .brand-name{font-family:"Raleway",sans-serif;font-weight:600;color:var(--purple);font-size:10px}
  .cover-band{position:absolute;left:0;top:113px;width:326px;height:32px;background:var(--purple);
    clip-path:polygon(0 0,88% 0,100% 100%,0 100%);display:flex;align-items:center;padding-left:10px}
  .cover-title{font-family:"Raleway",sans-serif;font-weight:600;color:var(--white);font-size:14.5px;letter-spacing:.2px}

  /* shared content slide parts */
  .slide-head{position:absolute;left:10px;top:10px;right:10px;display:flex;align-items:center;gap:5px}
  .slide-heading{font-family:"Raleway",sans-serif;font-weight:700;font-size:10px;white-space:nowrap}
  .slide-heading em{font-style:normal;color:var(--teal)}
  .head-rule{flex:1;height:1px;background:var(--purple)}
  .head-mark{font-family:"Raleway",sans-serif;font-weight:600;color:var(--purple);font-size:4.5px;width:22px;text-align:center;line-height:1.1}
  .slide-foot{position:absolute;left:0;bottom:0;width:100%;height:17px;background:var(--ink);display:flex;align-items:center;padding-left:10px}
  .web{color:var(--white);font-size:4.5px;letter-spacing:1px}
  .page-tab{position:absolute;right:0;bottom:0;width:20px;height:17px;background:var(--teal);clip-path:polygon(0 0,100% 0,100% 100%)}
  .page-num{position:absolute;right:2px;bottom:6px;font-size:4px;color:var(--white)}
  .fine{font-size:3.8px;line-height:1.55;color:var(--grey-text)}
  .item-title{font-size:4px;font-weight:700;color:var(--purple);text-decoration:underline}

  /* contents */
  .toc{position:absolute;left:46px;top:54px;width:280px;list-style:none}
  .toc li{display:flex;align-items:center;height:14px;font-size:4.3px;color:var(--grey-text)}
  .toc .entry{width:124px}
  .toc .sub{padding-left:8px}
  .toc .sub::before{content:"";display:inline-block;width:3px;height:3px;border-radius:50%;background:var(--teal);margin-right:4px;vertical-align:middle}
  .toc .leader{flex:1;border-bottom:1px dashed #bdbdbd;margin:0 12px 0 8px}
  .toc .num{width:10px;text-align:right}

  /* grid of items */
  .item-grid{position:absolute;left:28px;top:56px;display:grid;grid-template-columns:repeat(3,104px);row-gap:34px}
  .item{display:flex;gap:5px}
  .num-flag{flex:none;width:18px;height:18px;background:var(--teal);clip-path:polygon(0 0,100% 0,100% 100%);position:relative}
  .num-flag span{position:absolute;right:3px;top:2px;font-size:4.5px;color:var(--white);font-weight:700}
  .icon-box{flex:none;width:18px;height:18px;background:var(--teal);border-radius:2px;display:flex;align-items:center;justify-content:center}
  .item-text{width:60px}

  /* presenter layout */
  .person-photo{position:absolute;left:0;top:26px;width:142px;height:108px;
    background:linear-gradient(180deg,#f7f7f7 0%,#e6e8ea 55%,#cfd5dc 100%)}
  .note-band{position:absolute;left:0;top:122px;width:168px;height:32px;background:var(--purple);
    clip-path:polygon(0 0,100% 0,86% 100%,0 100%);padding:4px 26px 0 8px}
  .note-band p{font-size:3.6px;line-height:1.55;color:var(--white)}
  .side-notes{position:absolute;left:192px;top:53px;width:124px}
  .side-notes .block{margin-bottom:12px}
  .block-title{font-size:4px;font-weight:700;color:var(--teal)}

  /* cycle diagram */
  .cycle{position:absolute;left:20px;top:36px}
  .steps{position:absolute;left:177px;top:40px;width:140px}
  .steps-title{font-family:"Raleway",sans-serif;font-weight:700;font-size:6.5px;margin-bottom:7px}
  .steps-title em{font-style:normal;color:var(--teal)}
  .step{margin-bottom:6px}
</style>
</head>
<body>
  <div class="stage-top"></div>

  <!-- featured cover -->
  <section class="slide slide--hero">
    <div class="cover-photo" role="img" aria-label="Photo of a smiling businesswoman on the phone at a bright desk with plants"></div>
    <div class="cover-brand"><span class="brand-dot"></span><span class="brand-name">Meadowlark Crossing</span></div>
    <div class="cover-band"><h1 class="cover-title">PRESENTATION TITLE GOES HERE</h1></div>
  </section>

  <!-- 1 cover -->
  <section class="slide pos-1">
    <div class="cover-photo" role="img" aria-label="Photo of a smiling businesswoman on the phone at a bright desk with plants"></div>
    <div class="cover-brand"><span class="brand-dot"></span><span class="brand-name">Meadowlark Crossing</span></div>
    <div class="cover-band"><h2 class="cover-title">PRESENTATION TITLE GOES HERE</h2></div>
  </section>

  <!-- 2 contents -->
  <section class="slide pos-2">
    <header class="slide-head"><h2 class="slide-heading">TABLE OF <em>CONTENT</em></h2><span class="head-rule"></span><span class="head-mark">Meadowlark Crossing</span></header>
    <ol class="toc">
      <li><span class="entry">Lorem ipsum is simply dummy text of the printing</span><span class="leader"></span><span class="num">03</span></li>
      <li><span class="entry sub">Lorem ipsum is simply dummy text</span><span class="leader"></span><span class="num">04</span></li>
      <li><span class="entry sub">Lorem ipsum is simply dummy text</span><span class="leader"></span><span class="num">05</span></li>
      <li><span class="entry">Lorem ipsum is simply dummy text of the printing</span><span class="leader"></span><span class="num">06</span></li>
      <li><span class="entry">Lorem ipsum is simply dummy text of the printing</span><span class="leader"></span><span class="num">07</span></li>
      <li><span class="entry">Lorem ipsum is simply dummy text of the printing</span><span class="leader"></span><span class="num">08</span></li>
      <li><span class="entry sub">Lorem ipsum is simply dummy text</span><span class="leader"></span><span class="num">09</span></li>
      <li><span class="entry">Lorem ipsum is simply dummy text of the printing</span><span class="leader"></span><span class="num">10</span></li>
    </ol>
    <footer class="slide-foot"><span class="web">www.webaddress.com</span><span class="page-tab"></span><span class="page-num">2</span></footer>
  </section>

  <!-- 3 numbered points -->
  <section class="slide pos-3">
    <header class="slide-head"><h2 class="slide-heading">HEADLINE <em>GOES HERE</em></h2><span class="head-rule"></span><span class="head-mark">Meadowlark Crossing</span></header>
    <div class="item-grid">
      <div class="item"><span class="num-flag"><span>1</span></span><div class="item-text"><p class="item-title">YOUR TITLE HERE</p><p class="fine">Lorem ipsum is simply dummy text of the printing &amp; typesetting industry.</p></div></div>
      <div class="item"><span class="num-flag"><span>2</span></span><div class="item-text"><p class="item-title">YOUR TITLE HERE</p><p class="fine">Lorem ipsum is simply dummy text of the printing &amp; typesetting industry.</p></div></div>
      <div class="item"><span class="num-flag"><span>3</span></span><div class="item-text"><p class="item-title">YOUR TITLE HERE</p><p class="fine">Lorem ipsum is simply dummy text of the printing &amp; typesetting industry.</p></div></div>
      <div class="item"><span class="num-flag"><span>4</span></span><div class="item-text"><p class="item-title">YOUR TITLE HERE</p><p class="fine">Lorem ipsum is simply dummy text of the printing &amp; typesetting industry.</p></div></div>
      <div class="item"><span class="num-flag"><span>5</span></span><div class="item-text"><p class="item-title">YOUR TITLE HERE</p><p class="fine">Lorem ipsum is simply dummy text of the printing &amp; typesetting industry.</p></div></div>
      <div class="item"><span class="num-flag"><span>6</span></span><div class="item-text"><p class="item-title">YOUR TITLE HERE</p><p class="fine">Lorem ipsum is simply dummy text of the printing &amp; typesetting industry.</p></div></div>
    </div>
    <footer class="slide-foot"><span class="web">www.webaddress.com</span><span class="page-tab"></span><span class="page-num">3</span></footer>
  </section>

  <!-- 4 presenter -->
  <section class="slide pos-4">
    <header class="slide-head"><h2 class="slide-heading">HEADLINE <em>GOES HERE</em></h2><span class="head-rule"></span><span class="head-mark">Meadowlark Crossing</span></header>
    <div class="person-photo" role="img" aria-label="Photo of a man in glasses working on a laptop"></div>
    <div class="note-band"><p>Lorem ipsum is simply dummy text of the printing and typesetting industry, the standard dummy text ever since the 1500s when a printer took a galley of type.</p></div>
    <div class="side-notes">
      <div class="block"><p class="block-title">YOUR TITLE HERE</p><p class="fine">Lorem ipsum is simply dummy text of the printing and typesetting industry, standard since the 1500s.</p></div>
      <div class="block"><p class="block-title">YOUR TITLE HERE</p><p class="fine">Lorem ipsum is simply dummy text of the printing and typesetting industry, standard since the 1500s.</p></div>
      <div class="block"><p class="block-title">YOUR TITLE HERE</p><p class="fine">Lorem ipsum is simply dummy text of the printing and typesetting industry, standard since the 1500s.</p></div>
    </div>
    <footer class="slide-foot"><span class="web">www.webaddress.com</span><span class="page-tab"></span><span class="page-num">4</span></footer>
  </section>

  <!-- 5 icon points -->
  <section class="slide pos-5">
    <header class="slide-head"><h2 class="slide-heading">HEADLINE <em>GOES HERE</em></h2><span class="head-rule"></span><span class="head-mark">Meadowlark Crossing</span></header>
    <div class="item-grid">
      <div class="item"><span class="icon-box"><svg width="10" height="10" viewBox="0 0 10 10"><circle cx="5" cy="3" r="2" fill="#fff"/><path d="M1 10a4 4 0 0 1 8 0z" fill="#fff"/></svg></span><div class="item-text"><p class="item-title">YOUR TITLE HERE</p><p class="fine">Lorem ipsum is simply dummy text of the printing &amp; typesetting industry.</p></div></div>
      <div class="item"><span class="icon-box"><svg width="10" height="10" viewBox="0 0 10 10"><circle cx="5" cy="5" r="4" fill="none" stroke="#fff"/><path d="M1 5h8M5 1v8" stroke="#fff" stroke-width=".7"/></svg></span><div class="item-text"><p class="item-title">YOUR TITLE HERE</p><p class="fine">Lorem ipsum is simply dummy text of the printing &amp; typesetting industry.</p></div></div>
      <div class="item"><span class="icon-box"><svg width="10" height="10" viewBox="0 0 10 10"><circle cx="5" cy="5" r="4" fill="none" stroke="#fff"/><path d="M1 5h8M5 1v8" stroke="#fff" stroke-width=".7"/></svg></span><div class="item-text"><p class="item-title">YOUR TITLE HERE</p><p class="fine">Lorem ipsum is simply dummy text of the printing &amp; typesetting industry.</p></div></div>
      <div class="item"><span class="icon-box"><svg width="10" height="10" viewBox="0 0 10 10"><circle cx="5" cy="3" r="2" fill="#fff"/><path d="M1 10a4 4 0 0 1 8 0z" fill="#fff"/></svg></span><div class="item-text"><p class="item-title">YOUR TITLE HERE</p><p class="fine">Lorem ipsum is simply dummy text of the printing &amp; typesetting industry.</p></div></div>
      <div class="item"><span class="icon-box"><svg width="10" height="10" viewBox="0 0 10 10"><circle cx="5" cy="5" r="4" fill="none" stroke="#fff"/><path d="M1 5h8M5 1v8" stroke="#fff" stroke-width=".7"/></svg></span><div class="item-text"><p class="item-title">YOUR TITLE HERE</p><p class="fine">Lorem ipsum is simply dummy text of the printing &amp; typesetting industry.</p></div></div>
      <div class="item"><span class="icon-box"><svg width="10" height="10" viewBox="0 0 10 10"><circle cx="5" cy="5" r="4" fill="none" stroke="#fff"/><path d="M1 5h8M5 1v8" stroke="#fff" stroke-width=".7"/></svg></span><div class="item-text"><p class="item-title">YOUR TITLE HERE</p><p class="fine">Lorem ipsum is simply dummy text of the printing &amp; typesetting industry.</p></div></div>
    </div>
    <footer class="slide-foot"><span class="web">www.webaddress.com</span><span class="page-tab"></span><span class="page-num">5</span></footer>
  </section>

  <!-- 6 cycle -->
  <section class="slide pos-6">
    <header class="slide-head"><h2 class="slide-heading">HEADLINE <em>GOES HERE</em></h2><span class="head-rule"></span><span class="head-mark">Meadowlark Crossing</span></header>
    <svg class="cycle" width="130" height="130" viewBox="0 0 130 130">
      <circle cx="65" cy="65" r="44" fill="none" stroke="var(--purple)" stroke-width="9"/>
      <g fill="var(--teal)" stroke="#fff" stroke-width="2">
        <circle cx="65" cy="19" r="15"/><circle cx="19" cy="65" r="15"/>
        <circle cx="111" cy="65" r="15"/><circle cx="65" cy="111" r="15"/>
      </g>
      <g fill="#fff">
        <circle cx="65" cy="16" r="3"/><path d="M59 26a6 6 0 0 1 12 0z"/>
        <circle cx="19" cy="62" r="3"/><path d="M13 72a6 6 0 0 1 12 0z"/>
      </g>
      <g fill="none" stroke="#fff" stroke-width="1.2">
        <circle cx="111" cy="65" r="6"/><path d="M105 65h12M111 59v12"/>
        <circle cx="65" cy="111" r="6"/><path d="M59 111h12M65 105v12"/>
      </g>
      <text x="65" y="63" text-anchor="middle" font-family="Raleway, sans-serif" font-weight="600" font-size="7" fill="var(--purple)">Meadowlark</text>
      <text x="65" y="72" text-anchor="middle" font-family="Raleway, sans-serif" font-weight="600" font-size="7" fill="var(--purple)">Crossing</text>
    </svg>
    <div class="steps">
      <p class="steps-title">Title <em>Goes Here</em></p>
      <div class="step"><p class="block-title">STEP - 1</p><p class="fine">Lorem ipsum is simply dummy text of the printing and typesetting industry standard.</p></div>
      <div class="step"><p class="block-title">STEP - 2</p><p class="fine">Lorem ipsum is simply dummy text of the printing and typesetting industry standard.</p></div>
      <div class="step"><p class="block-title">STEP - 3</p><p class="fine">Lorem ipsum is simply dummy text of the printing and typesetting industry standard.</p></div>
      <div class="step"><p class="block-title">STEP - 4</p><p class="fine">Lorem ipsum is simply dummy text of the printing and typesetting industry standard.</p></div>
    </div>
    <footer class="slide-foot"><span class="web">www.webaddress.com</span><span class="page-tab"></span><span class="page-num">6</span></footer>
  </section>
</body>
</html>
```